Candle company needs a label for candle

Looking for a designer to create my candle label. I am going to attach a few pictures of my vision for the label as well as my Company Logo and jar I have puchased. I'm going for the modern rustic feel but you are the designer and have full trust in your abilities. The label is going to be printed on Kraft paper (2x3) so looking for the font to be black. The candle label MUST include the following information:
Candle Birchway Co.
NO. 01: Eucalyptus + Spearmint
Handmade In NJ
Soy Wax
9oz

Industry/Entity Type

Candle Industry

Colors

Designer to choose colors to be used in the design.

Requirements
Should not have
• Any images

```html
<!DOCTYPE html>
<html lang="en">
<head>
<meta charset="utf-8">
<title>Candle Birchway Co. — Candle Label</title>
<link href="https://fonts.googleapis.com/css2?family=Dancing+Script:wght@600&family=Share+Tech+Mono&display=swap" rel="stylesheet">
<style>
  :root {
    --backdrop: #f1f1f1;
    --kraft: #bba27d;
    --kraft-deep: #b09672;
    --ink: #111111;
    --shadow: rgba(0, 0, 0, 0.28);
  }
  * { margin: 0; padding: 0; box-sizing: border-box; }
  html, body {
    width: 1200px;
    height: 1200px;
    overflow: hidden;
    background: var(--backdrop);
  }
  .canvas {
    position: relative;
    width: 1200px;
    height: 1200px;
  }
  .label {
    position: absolute;
    left: 252px;
    top: 370px;
    width: 692px;
    height: 458px;
    background: radial-gradient(ellipse at 40% 40%, var(--kraft) 0%, var(--kraft-deep) 100%);
    box-shadow: 6px 8px 10px var(--shadow);
    color: var(--ink);
    text-align: center;
  }
  .brand-name {
    position: absolute;
    left: 0;
    right: 0;
    top: 90px;
    font-family: "Dancing Script", cursive;
    font-weight: 600;
    font-size: 86px;
    line-height: 1;
    letter-spacing: 1px;
  }
  .divider {
    position: absolute;
    left: 100px;
    top: 236px;
    width: 492px;
    height: 8px;
  }
  .scent-name {
    position: absolute;
    left: 0;
    right: 0;
    top: 256px;
    font-family: "Share Tech Mono", monospace;
    font-size: 27px;
    letter-spacing: 1.5px;
  }
  .details {
    position: absolute;
    left: 0;
    right: 0;
    top: 342px;
    list-style: none;
    font-family: "Share Tech Mono", monospace;
    font-size: 19px;
    line-height: 31px;
    letter-spacing: 1px;
  }
</style>
</head>
<body>
  <main class="canvas">
    <section class="label">
      <h1 class="brand-name">Candle Birchway Co.</h1>
      <svg class="divider" viewBox="0 0 492 8" aria-hidden="true">
        <line x1="0" y1="1" x2="492" y2="1" stroke="#111" stroke-width="1" stroke-dasharray="3 2"/>
        <line x1="0" y1="6" x2="492" y2="6" stroke="#111" stroke-width="1"/>
      </svg>
      <h2 class="scent-name">NO. 01: EUCALYPTUS + SPEARMINT</h2>
      <ul class="details">
        <li>HANDMADE IN NJ</li>
        <li>SOY WAX</li>
        <li>9OZ</li>
      </ul>
    </section>
  </main>
</body>
</html>
```